Law Firm Investment Immigration Brochure

I'm looking to have a brochure designed for my law firm. The brochure will be about investment immigration and will be designed to attract potential immigrations.
As this program is geared towards wealthier clients, I will need the winning brochure design to be classy.
The overall theme of my brochure should be to look simple, elegant, smart and professional.
I would like the delivery of the brochure in high-res PSD and AI formats in CS1 and CS3, which can be resized later to any resolution possible (print ready included). I will then own the rights to the content once the work has been paid for. I will need multiple formats - .psd (CS1 and CS3), .ai (CS1 and CS3), .jpg, and .gif.
I have included a copy of my logo design so please design the brochure accordingly.
The name of my law firm is "Law Offices of Marcel Dovrane".
Thanks in advance.
Updates
Even though my brochure is 1 page, I will be folding it twice, so that it looks like an "N". The side that clients will see first will act as the cover page. Therefore, on it, I would like you to include my logo design and then my office address (which I will supply to you later). My cover page would take up the right 1/3 of this design you will submit. Therefore, please submit a design which would take up the left 2/3 of the page, and then design a cover page that will take up the right 1/3 of the page. Just so you know, my brochure will be 2-sided, so please show me what both sides will look like. The back side of the brochure will have all written content, and no cover page. Therefore, please design the whole back side of the brochure as one, instead of the front side, which is split 2/3 and 1/3. Thank you in advance, Marc

```html
<!DOCTYPE html>
<html lang="en">
<head>
<meta charset="utf-8">
<title>Law Offices of Marcel Dovrane – Investment Immigration Brochure</title>
<link rel="stylesheet" href="https://fonts.googleapis.com/css2?family=Open+Sans:wght@400;600&display=swap">
<style>
  :root {
    --page-bg: #e6e7ea;
    --paper: #ffffff;
    --navy: #1d2d6b;
    --blue: #2f5fae;
    --blue-light: #a9c4e6;
    --sheen: #eef1f6;
    --text: #3a3f4a;
    --fold: #dfe3ea;
  }
  * { margin: 0; padding: 0; box-sizing: border-box; }
  html, body {
    width: 851px; height: 1200px; overflow: hidden;
    background: var(--page-bg);
    font-family: "Open Sans", Arial, sans-serif;
  }
  .spread {
    position: absolute; left: 20px; top: 327px;
    width: 811px; height: 546px;
    background: var(--paper);
    overflow: hidden;
    box-shadow: 0 2px 10px rgba(0,0,0,0.18);
  }
  .spread-art { position: absolute; inset: 0; }
  .column {
    position: absolute; width: 226px;
    color: var(--text); font-size: 9.4px; line-height: 1.5;
    text-align: justify;
  }
  .column p + p { margin-top: 22px; }
  .column--left { left: 24px; top: 26px; }
  .column--middle { left: 294px; top: 26px; }
  .column--middle p + p { margin-top: 70px; }
  .brand {
    position: absolute; right: 22px; top: 26px;
    display: flex; align-items: center; gap: 10px;
    color: var(--navy); font-weight: 600; text-transform: uppercase;
  }
  .brand-square { width: 14px; height: 14px; background: var(--navy); }
  .brand-name { text-align: right; line-height: 1.15; }
  .brand-name .lead { display: block; font-size: 8.5px; letter-spacing: 1.6px; }
  .brand-name .firm { display: block; font-size: 19px; letter-spacing: 0.6px; }
  .cover-visual {
    position: absolute; left: 572px; top: 110px;
    width: 214px; height: 220px; border-radius: 4px;
    background: linear-gradient(155deg, #2a3550 0%, #141a2a 60%, #5a2430 100%);
  }
  .contact {
    position: absolute; right: 24px; bottom: 20px; width: 200px;
    color: #ffffff; font-size: 9px; line-height: 1.5;
  }
  .contact strong { font-weight: 600; }
</style>
</head>
<body>
  <section class="spread">
    <svg class="spread-art" viewBox="0 0 811 546" width="811" height="546" aria-hidden="true">
      <defs>
        <linearGradient id="waveDeep" x1="0" y1="1" x2="1" y2="0">
          <stop offset="0" stop-color="#1d2d6b"/>
          <stop offset="1" stop-color="#2f5fae"/>
        </linearGradient>
        <linearGradient id="waveSoft" x1="0" y1="0" x2="1" y2="0">
          <stop offset="0" stop-color="#ffffff" stop-opacity="0"/>
          <stop offset="1" stop-color="#a9c4e6"/>
        </linearGradient>
      </defs>
      <polygon points="120,0 300,0 60,546 0,546 0,380" fill="var(--sheen)"/>
      <polygon points="430,0 560,0 360,546 250,546" fill="var(--sheen)" opacity="0.8"/>
      <line x1="270" y1="0" x2="270" y2="546" stroke="var(--fold)" stroke-width="1"/>
      <line x1="540" y1="0" x2="540" y2="546" stroke="var(--fold)" stroke-width="1"/>
      <path d="M180,546 C360,470 560,430 811,330 L811,546 Z" fill="url(#waveSoft)"/>
      <path d="M250,546 C420,490 600,440 811,380 L811,546 Z" fill="var(--blue-light)" opacity="0.7"/>
      <path d="M330,546 C480,505 640,460 811,420 L811,546 Z" fill="url(#waveDeep)"/>
      <path d="M300,530 C460,480 640,430 811,395" fill="none" stroke="#ffffff" stroke-width="1.5" opacity="0.8"/>
    </svg>

    <div class="column column--left">
      <p>Investment immigration offers qualified families a clear route to permanent residence through a substantial, approved investment. Our firm guides each client from the first consultation through every filing, review and interview, so that the process stays orderly, discreet and predictable. We assess source of funds, prepare complete documentation and keep you informed at each stage of the application.</p>
      <p>Every investor arrives with different goals. Some wish to expand a business abroad, others to secure education and opportunity for their children. We listen first, then design a strategy that fits your capital, your timeline and your family, drawing on years of careful practice in immigration law.</p>
    </div>

    <div class="column column--middle">
      <p>Our attorneys review each proposed investment with care, confirming that it meets program rules before any funds are committed. We coordinate with accountants, banks and regional centers so that nothing is left to chance, and we respond promptly to every request from the authorities.</p>
      <p>Confidentiality is central to our work. Personal and financial details are handled privately and shared only where the law requires. Contact our office to arrange a consultation and learn how investment immigration can open a new chapter for you and your family.</p>
    </div>

    <div class="brand">
      <span class="brand-square"></span>
      <span class="brand-name">
        <span class="lead">Law Offices of</span>
        <span class="firm">Marcel Dovrane</span>
      </span>
    </div>

    <div class="cover-visual" role="img" aria-label="Photograph of a dark navy passport with a rising red growth arrow"></div>

    <div class="contact">
      <strong>Address:</strong> 210 Harbour Lane, Suite 4, Brookvale, NY 10021<br>
      Phone: (555) 014-2290
    </div>
  </section>
</body>
</html>
```